Business Card Design Project

KV Strategy Partners is a management consulting business with C-suite (CEO/CFO etc) target clients. Logo selected is blue with simple/serious typefaces.

Target Market(s)

CEOs and CFOs of large corporates

Industry/Entity Type

Management Consulting

Font styles to use
Serif

Colors
3276b5

Requirements
Must have
• Tag line: Clear counsel for lasting growth (use different font)
Address: 457 Cedar Brook Lane #03-22 Singapore 519307
Telephone: +65 8372 6094
Email: kvlorne@mailbox47.com

```html
<!DOCTYPE html>
<html lang="en">
<head>
<meta charset="utf-8">
<title>KV Strategy Partners — Business Cards</title>
<link rel="stylesheet" href="https://fonts.googleapis.com/css2?family=Cinzel:wght@500&family=Montserrat:wght@400;700&display=swap">
<style>
  :root {
    --brand-blue: #2b3990;
    --paper: #ffffff;
    --backdrop: #ececec;
    --shadow: rgba(0, 0, 0, 0.12);
  }
  * { box-sizing: border-box; margin: 0; padding: 0; }
  html, body {
    width: 1200px; height: 1000px; overflow: hidden;
    background: var(--backdrop);
  }
  .canvas {
    position: relative; width: 1200px; height: 1000px;
    display: flex; align-items: center; justify-content: center; gap: 60px;
  }
  .card {
    position: relative; width: 525px; height: 300px;
    box-shadow: 0 8px 24px var(--shadow);
    overflow: hidden;
  }

  /* Contact side */
  .card--contact { background: var(--paper); color: var(--brand-blue); }
  .card--contact .wordmark {
    position: absolute; left: 40px; top: 36px;
    font-family: "Cinzel", serif; font-weight: 500; font-size: 18px;
    letter-spacing: 1px; color: var(--brand-blue); white-space: nowrap;
  }
  .address {
    position: absolute; right: 36px; top: 104px;
    font-family: "Montserrat", sans-serif; font-size: 12px; letter-spacing: 0.8px;
    line-height: 1.45; display: flex; gap: 6px; align-items: flex-start;
  }
  .address svg { width: 11px; height: 14px; margin-top: 1px; flex: none; }
  .person {
    position: absolute; left: 40px; top: 168px;
    display: flex; align-items: stretch; gap: 12px;
    font-family: "Montserrat", sans-serif;
  }
  .person__id { text-align: right; }
  .person__name { font-weight: 700; font-size: 18px; letter-spacing: 0.5px; line-height: 1.15; }
  .person__title { font-weight: 400; font-size: 12px; letter-spacing: 1.5px; }
  .person__rule { width: 1.5px; background: var(--brand-blue); }
  .contact-list { list-style: none; display: flex; flex-direction: column; gap: 6px; justify-content: center; }
  .contact-list li { display: flex; align-items: center; gap: 8px; font-size: 12px; letter-spacing: 0.8px; white-space: nowrap; }
  .contact-list svg { width: 16px; height: 16px; flex: none; }
  .band { position: absolute; left: 0; bottom: 0; width: 100%; height: 22px; }

  /* Brand side */
  .card--brand {
    background: var(--brand-blue); color: var(--paper);
    display: flex; flex-direction: column; align-items: center; justify-content: center; gap: 10px;
  }
  .card--brand .wordmark {
    font-family: "Cinzel", serif; font-weight: 500; font-size: 28px;
    letter-spacing: 1.5px; color: var(--paper); white-space: nowrap;
  }
  .tagline {
    font-family: "Montserrat", sans-serif; font-weight: 400; font-size: 10px;
    letter-spacing: 2.6px; text-transform: uppercase;
  }
</style>
</head>
<body>
<main class="canvas">
  <section class="card card--contact" aria-label="Contact side of business card">
    <div class="wordmark">KV Strategy Partners</div>

    <div class="address">
      <svg viewBox="0 0 11 14" aria-hidden="true"><path d="M5.5 0A5 5 0 0 0 .5 5c0 3.6 5 9 5 9s5-5.4 5-9a5 5 0 0 0-5-5zm0 7A2 2 0 1 1 5.5 3a2 2 0 0 1 0 4z" fill="currentColor"/></svg>
      <p>457 CEDAR BROOK LANE<br>#03-22 SINGAPORE 519307</p>
    </div>

    <div class="person">
      <div class="person__id">
        <p class="person__name">YOUR NAME</p>
        <p class="person__title">YOUR TITLE</p>
      </div>
      <span class="person__rule"></span>
      <ul class="contact-list">
        <li>
          <svg viewBox="0 0 16 16" aria-hidden="true"><circle cx="8" cy="8" r="8" fill="currentColor"/><path d="M6 4.2l1 2.2-.8.8a5 5 0 0 0 2.6 2.6l.8-.8 2.2 1-.4 1.6C8 11.6 4.4 8 4.4 4.6z" fill="#fff"/></svg>
          +65 8372 6094
        </li>
        <li>
          <svg viewBox="0 0 16 16" aria-hidden="true"><circle cx="8" cy="8" r="8" fill="currentColor"/><rect x="4" y="5" width="8" height="6" fill="none" stroke="#fff" stroke-width="1"/><path d="M4 5l4 3.2L12 5" fill="none" stroke="#fff" stroke-width="1"/></svg>
          KVLORNE@MAILBOX47.COM
        </li>
      </ul>
    </div>

    <svg class="band" viewBox="0 0 525 22" preserveAspectRatio="none" aria-hidden="true">
      <rect x="0" y="0" width="525" height="22" fill="var(--brand-blue)"/>
      <polygon points="228,22 236,22 250,0 242,0" fill="var(--paper)"/>
    </svg>
  </section>

  <section class="card card--brand" aria-label="Brand side of business card">
    <div class="wordmark">KV Strategy Partners</div>
    <p class="tagline">Clear counsel for lasting growth</p>
  </section>
</main>
</body>
</html>
```